Velmora, Inc. Website

Looking for a website design and build for Velmora, Inc. an intellectual property incubator for the recreational and medical cannabis space in California. Our logo and brand identity has been completed website so w can begin our SEO leg of brand development.

See more details in Must haves and Nice to Haves

Target Market(s)

Target market

Vision

Our proprietary ideas have been developed to shift the approach on how whole body wellness and healing is achieved. Velmora's patent pending designs and formulations are rooted in the desire to find the most efficient, customizable, and convenient  method to precisely micro-despense whole plant cannabis extracts. 

Our ideas, designs and development team are supported by leading chemists specializing in cannabis extraction technology, leading medical doctors collaborating to develop our proprietary cannabis formulations and a passion to shift landscape of healing from a dependency on isolated symptom treatment to whole body, whole plant, whole life wellness for ourselves and our families. 

Goal

Develop, patent, and trademark our proprietary devices, formulations, and ideas for the purpose of licensing, manufacturing and distributing in the Cannabis Industry.

Industry/Entity Type

Medical

Coding

Coded - Design and coding required

Number of Pages Required

5+ page

Font styles to use
Other font styles liked:
• See Brand Identity Guide

Requirements
Must have
• Look and Feel: We are developing products, intellectual property and platforms to bring together the medical, health & wellness, and cannabis industries to provide individuals and families alike a innovative solutions to chronic illness, mood disorders, and over all wellbeing.
• Page Titles
• Home - Landing Page
• Vision-
• IP Technology & Products - will remain under construction
• Team
• Strategic Partners – will remain under construction
• Invest- will need a form to aquire contact information as well as have some questions that need to be answered to help evaluate to the potential interested party
• Contact Us– Velmora address and info@ email
Nice to have
• Images - wellness, balance, health, healing, herbs, not just cannabis, aromatherapy, mediation, energy work, dna, scientific research, microdosing, medical testing
• Style sleek and innovative - cutting edge technology - inspire to learn more
• For Colors and Fonts - See Brand Identity Guide
• Site layouts that we like are:
• http://www.thepravexgroup.example
• https://www.duneloftcare.example
• https://www.sorvanti.example
• https://www.quolt.example
• https://www.tarefy.example
Should not have
• Should not have to many cannabis images - imagery should balanced between cannabis, medical & recreational, health and wellness, mental health

```html
<!DOCTYPE html>
<html lang="en">
<head>
<meta charset="utf-8">
<title>Velmora, Inc. Website</title>
<link href="https://fonts.googleapis.com/css2?family=Jost:wght@300;400;500&display=swap" rel="stylesheet">
<style>
  :root {
    --backdrop: #ecebdf;
    --page-white: #ffffff;
    --page-mist: #efefef;
    --ink: #1d1d1d;
    --ink-soft: #4a4a4a;
    --photo-dark: #3f3f3f;
    --photo-mid: #777777;
    --photo-light: #a9a9a9;
    --brand-purple: #7b3f98;
    --brand-green: #3c9a43;
    --leaf-green: #3f6b2a;
    --map-grey: #e2e2e2;
  }
  * { box-sizing: border-box; margin: 0; padding: 0; }
  html, body { width: 1200px; height: 900px; overflow: hidden; }
  body {
    background: var(--backdrop);
    font-family: "Jost", "Helvetica Neue", Arial, sans-serif;
    color: var(--ink);
    position: relative;
  }
  .page {
    position: absolute;
    top: 30px;
    width: 500px;
    height: 840px;
    background: var(--page-white);
    overflow: hidden;
    box-shadow: 0 10px 30px rgba(0,0,0,.12);
  }
  .page--inner { left: 70px; }
  .page--home { left: 630px; }

  /* shared bits */
  .section-title {
    font-weight: 300;
    letter-spacing: 2px;
    text-transform: uppercase;
  }
  .band-title {
    font-weight: 300;
    font-size: 26px;
    color: #fff;
    letter-spacing: .5px;
  }
  .band-rule {
    width: 54px; height: 1px;
    background: var(--brand-green);
    margin: 6px auto 10px;
  }
  .band-copy {
    font-size: 8.5px;
    line-height: 1.45;
    color: #eaeaea;
    letter-spacing: .4px;
    max-width: 210px;
    margin: 0 auto;
  }
  .round-link {
    width: 16px; height: 16px;
    margin: 12px auto 0;
    display: block;
  }
  .brand-name {
    font-weight: 400;
    letter-spacing: 2px;
    color: var(--ink);
    text-transform: uppercase;
  }

  /* inner page */
  .photo-band {
    position: relative;
    height: 170px;
    background: linear-gradient(120deg, var(--photo-dark), var(--photo-mid) 60%, #555 100%);
    text-align: center;
    padding-top: 36px;
  }
  .intro {
    height: 220px;
    padding: 44px 40px 0 250px;
    text-align: right;
    background: linear-gradient(90deg, #fff 0%, #fff 60%, #f1f1f1 100%);
  }
  .intro .section-title { font-size: 20px; margin-bottom: 14px; }
  .intro p { font-size: 8.5px; line-height: 1.5; color: var(--ink-soft); letter-spacing: .4px; }
  .partners {
    height: 90px;
    background: #f6f6f6;
    display: flex;
    align-items: center;
    padding: 0 40px;
    gap: 40px;
  }
  .partners__label { font-size: 11px; letter-spacing: 1px; color: var(--ink-soft); }
  .partners__label::after {
    content: ""; display: block; width: 10px; height: 1px;
    background: var(--brand-purple); margin-top: 4px;
  }
  .partner-badge { width: 34px; height: 34px; background: #555; }
  .partner-badge--round { border-radius: 50%; background: #444; }
  .partner-badge--square { background: #333; }
  .map {
    height: 190px;
    background: linear-gradient(135deg, var(--map-grey), #d6d6d6);
  }
  .site-footer {
    height: 170px;
    background: #f0f0f0;
    display: flex;
    align-items: center;
    justify-content: center;
  }
  .site-footer .brand-name { font-size: 18px; }

  /* home page */
  .site-nav {
    height: 50px;
    background: var(--page-mist);
    display: flex;
    align-items: center;
    justify-content: center;
    gap: 16px;
    font-size: 8px;
    letter-spacing: .5px;
    color: var(--ink-soft);
  }
  .site-nav .is-current { border-bottom: 1px solid var(--brand-purple); }
  .site-nav .brand-name { font-size: 9px; letter-spacing: 1px; }
  .hero {
    position: relative;
    height: 230px;
    background: var(--page-mist);
    text-align: center;
    padding-top: 40px;
  }
  .hero .section-title { font-size: 28px; margin-bottom: 12px; }
  .hero p {
    font-size: 8px; line-height: 1.5; color: var(--ink-soft);
    max-width: 200px; margin: 0 auto; letter-spacing: .3px;
  }
  .button-outline {
    display: inline-block;
    margin-top: 28px;
    border: 1px solid var(--ink);
    padding: 3px 16px;
    font-size: 6px; letter-spacing: 1px;
  }
  .leaf {
    position: absolute;
    background: radial-gradient(circle at 40% 40%, #5b8a3c, var(--leaf-green));
    border-radius: 60% 10% 60% 10%;
  }
  .leaf--top { top: -20px; right: -30px; width: 150px; height: 150px; }
  .leaf--low { bottom: -30px; left: -30px; width: 80px; height: 80px; }
  .vision {
    height: 250px;
    padding-top: 34px;
    text-align: center;
  }
  .vision .section-title { font-size: 28px; margin-bottom: 18px; }
  .vision__body { display: flex; align-items: center; justify-content: center; gap: 12px; padding: 0 30px; }
  .vision__copy {
    width: 180px;
    font-size: 7.5px; line-height: 1.5; color: var(--ink-soft);
    text-align: center; letter-spacing: .3px;
  }
  .vision__arrow { display: block; margin: 4px 0 0 auto; width: 12px; height: 6px; }
  .vision__art {
    width: 200px; height: 130px;
    background: linear-gradient(90deg, #2f9a3b 0%, #333 35%, #5a2a7a 65%, #9a9a9a 100%);
    border-radius: 60px 20px 60px 20px;
    opacity: .9;
  }
  .split-band { position: relative; height: 310px; }
  .split-band__photo { position: absolute; inset: 0; }
  .split-band__photo--upper {
    clip-path: polygon(0 0, 100% 0, 100% 80%, 0 33%);
    background: linear-gradient(160deg, var(--photo-mid), var(--photo-dark) 70%, #222);
  }
  .split-band__photo--lower {
    clip-path: polygon(0 33%, 100% 80%, 100% 100%, 0 100%);
    background: linear-gradient(200deg, var(--photo-light), var(--photo-mid) 45%, var(--photo-dark));
  }
  .split-band__divider { position: absolute; inset: 0; width: 100%; height: 100%; }
  .split-band__text { position: absolute; text-align: center; width: 240px; }
  .split-band__text--upper { top: 22px; right: 30px; }
  .split-band__text--lower { bottom: 20px; left: 24px; }
</style>
</head>
<body>

<section class="page page--inner">
  <div class="photo-band" role="img" aria-label="Dark wellness photograph behind the section heading">
    <h2 class="band-title">- Lorem Ipsum -</h2>
    <div class="band-rule"></div>
    <p class="band-copy">Sed egestas, sem a ornare imperdiet, dui nisi convallis ex, a luctus metus erat vel nibh. Pellentesque magna dolor, auctor at nisl ac, scelerisque suscipit eros.</p>
    <svg class="round-link" viewBox="0 0 16 16"><circle cx="8" cy="8" r="7" fill="none" stroke="#fff" stroke-width="1"/><path d="M6 5l4 3-4 3" fill="none" stroke="#fff" stroke-width="1"/></svg>
  </div>

  <div class="intro">
    <h2 class="section-title">Lorem Ipsum</h2>
    <p>Sed egestas, sem a ornare convallis ex, tesque magna dolor.</p>
  </div>

  <div class="partners">
    <span class="partners__label">Strategic partners</span>
    <span class="partner-badge partner-badge--round" aria-hidden="true"></span>
    <span class="partner-badge partner-badge--square" aria-hidden="true"></span>
  </div>

  <div class="map" role="img" aria-label="Street map showing the office location"></div>

  <footer class="site-footer">
    <span class="brand-name">Velmora</span>
  </footer>
</section>

<section class="page page--home">
  <nav class="site-nav">
    <span class="is-current">Home</span>
    <span>Vision</span>
    <span class="brand-name">Velmora</span>
    <span>Team</span>
    <span>Invest</span>
    <span>Contact Us</span>
  </nav>

  <header class="hero">
    <div class="leaf leaf--top" role="img" aria-label="Cannabis leaf photograph"></div>
    <div class="leaf leaf--low" role="img" aria-label="Cannabis leaf photograph"></div>
    <h1 class="section-title">Lorem Ipsum</h1>
    <p>Lorem ipsum dolor sit amet, consectetur adipiscing elit. Sed placerat libero in diam commodo mattis. In leo mi, aliquet vitae erat nec, nec vehicula varius massa. Fusce id quam ac justo consectetur porttitor sed quis ex. Lorem ipsum dolor sit amet, consectetur adipiscing elit.</p>
    <span class="button-outline">LEARN MORE</span>
  </header>

  <section class="vision">
    <h2 class="section-title">Vision</h2>
    <div class="vision__body">
      <div class="vision__copy">
        <p>Lorem ipsum dolor sit amet, consectetur adipiscing elit. Sed placerat libero in diam commodo mattis. In leo mi, aliquet vitae erat nec, malesuada varius massa. Fusce id quam ac justo consectetur porttitor sed quis ex. Lorem ipsum dolor sit amet, consectetur adipiscing elit. Fusce id quam ac justo consectetur porttitor sed quis ex. Lorem ipsum dolor sit amet, consectetur.</p>
        <svg class="vision__arrow" viewBox="0 0 12 6"><path d="M0 3h10M8 1l2 2-2 2" fill="none" stroke="#1d1d1d" stroke-width="1"/></svg>
      </div>
      <div class="vision__art" role="img" aria-label="Illustrated DNA double helix in green, purple and grey"></div>
    </div>
  </section>

  <section class="split-band">
    <div class="split-band__photo split-band__photo--upper" role="img" aria-label="Photograph of a person meditating beside a lake"></div>
    <div class="split-band__photo split-band__photo--lower" role="img" aria-label="Photograph of hands preparing herbal remedies in jars"></div>
    <svg class="split-band__divider" viewBox="0 0 500 310" preserveAspectRatio="none" aria-hidden="true"><line x1="0" y1="102" x2="500" y2="248" stroke="#fff" stroke-width="3"/></svg>

    <div class="split-band__text split-band__text--upper">
      <h2 class="band-title">- Lorem Ipsum -</h2>
      <div class="band-rule"></div>
      <p class="band-copy">Sed egestas, sem a ornare imperdiet, dui nisi convallis ex, a luctus metus erat vel nibh. Pellentesque magna dolor, auctor at nisl ac, scelerisque suscipit eros.</p>
      <svg class="round-link" viewBox="0 0 16 16"><circle cx="8" cy="8" r="7" fill="none" stroke="#fff" stroke-width="1"/><path d="M6 5l4 3-4 3" fill="none" stroke="#fff" stroke-width="1"/></svg>
    </div>

    <div class="split-band__text split-band__text--lower">
      <h2 class="band-title">- Lorem Ipsum -</h2>
      <div class="band-rule"></div>
      <p class="band-copy">Sed egestas, sem a ornare imperdiet, dui nisi convallis ex, a luctus metus erat vel nibh. Pellentesque magna dolor, auctor at nisl ac, scelerisque suscipit eros.</p>
      <svg class="round-link" viewBox="0 0 16 16"><circle cx="8" cy="8" r="7" fill="none" stroke="#fff" stroke-width="1"/><path d="M6 5l4 3-4 3" fill="none" stroke="#fff" stroke-width="1"/></svg>
    </div>
  </section>
</section>

</body>
</html>
```